Law Firm Website (Designed in Wix)

A website designed using my Wix account.
A website for a generalist law firm based in Melbourne, Australia.
The areas of practice include:
Criminal Law
Family Law
Civil Litigation
Wills & Probate
BRUNE Claims
The colour theme will be green, black and white.
Website will require the following elements:
1. Chat box
2. General Description of the practice
3. Practice Areas (for selection)
4. Calendar bookings for Microsoft Outlook
5. Email enquiries
6. Telephone enquiries
7. Business location map
8. Videos
9. Photos

The following website can be used as inspiration, however I am looking for a copy and paste version of this site:
tarnwellcounsel.com

Target Market(s)

People requiring a Lawyer for Criminal, Family, Wills and Probabte, Conveyancing and Civil Litigstion Matters

Industry/Entity Type

Legal Sector

Coding

Coded - Design and coding required

Number of Pages Required

5+ page

Other font styles liked:
• Based on business card

Requirements
Must have
• Colours and theme based on business card

```html
<!DOCTYPE html>
<html lang="en">
<head>
<meta charset="utf-8">
<title>Kellbrook Lawyers</title>
<link href="https://fonts.googleapis.com/css2?family=Exo+2:wght@500;600;700&family=Lato:wght@400;700&display=swap" rel="stylesheet">
<style>
:root{
  --green:#0b7a17;
  --green-dark:#07600f;
  --ink:#111;
  --text:#444;
  --muted:#888;
  --light:#f2f2f2;
  --panel:#1a1a1a;
  --footer:#0d0d0d;
  --white:#fff;
  --star:#0b7a17;
}
*{box-sizing:border-box;margin:0;padding:0}
html,body{width:1200px;height:5314px;overflow:hidden}
body{position:relative;font-family:"Lato",Arial,sans-serif;color:var(--text);background:var(--white)}
.abs{position:absolute}
.head{font-family:"Exo 2",Arial,sans-serif;color:var(--ink)}
.btn-outline{position:absolute;border:1.5px solid var(--green);color:var(--ink);font-size:16px;display:flex;align-items:center;justify-content:center;gap:10px;background:var(--white)}
.centered{text-align:center;left:0;width:1200px}

/* hero */
.hero{left:0;top:0;width:1200px;height:775px;background:linear-gradient(160deg,#4a4a4a,#2f2f2f 55%,#3b3b3b)}
.brand{left:80px;top:28px;width:110px;text-align:center;color:var(--white);font-family:"Lato",sans-serif;font-weight:700;font-size:15px;line-height:1.1;letter-spacing:1px}
.brand .mark{width:34px;height:34px;border-radius:50%;border:2px solid var(--white);margin:0 auto 6px}
.nav{left:265px;top:48px;display:flex;gap:38px;color:#eee;font-size:15px}
.nav-phone{left:930px;top:45px;color:var(--white);font-weight:700;font-size:19px;display:flex;gap:8px;align-items:center}
.hero-title{top:425px;color:var(--white);font-size:64px;font-weight:600;line-height:74px}
.hero-btn{position:absolute;top:606px;height:42px;border:1.5px solid #ddd;color:var(--white);font-size:16px;display:flex;align-items:center;justify-content:center;gap:10px}
.hero-cta{top:694px;color:var(--white);font-family:"Exo 2",sans-serif;font-weight:600;font-size:21px}
.video-main{left:229px;top:738px;width:742px;height:380px;background:linear-gradient(180deg,#3d3d3d,#8a8a8a 55%,#5a5a5a)}
.play{position:absolute;border-radius:50%;background:var(--white);display:flex;align-items:center;justify-content:center}

/* welcome */
.welcome-h{top:1207px;font-size:30px;font-weight:600}
.welcome-sub{top:1272px;left:115px;width:970px;text-align:center;font-size:22px;line-height:34px;color:#333}
.col{top:1366px;width:468px;font-size:15.5px;line-height:29px;text-align:justify;color:#444}

/* reviews */
.reviews{left:0;top:1645px;width:1200px;height:268px;background:var(--light)}
.arrow-c{position:absolute;width:34px;height:34px;border:1.5px solid var(--green);border-radius:50%;display:flex;align-items:center;justify-content:center}
.review{position:absolute;top:60px;width:245px;font-size:14.5px;line-height:26px;color:#444}
.review .name{font-weight:700;color:var(--ink);margin:6px 0 4px}

/* stats */
.stat{position:absolute;top:2010px;width:300px;text-align:center;color:var(--muted);font-size:18px;line-height:26px}
.stat .num{font-family:"Exo 2",sans-serif;color:var(--ink);font-size:50px;font-weight:500;line-height:58px}

/* practice */
.practice{left:0;top:2231px;width:1200px;height:726px;background:linear-gradient(135deg,#ededed,#e3e3e3 50%,#ececec)}
.section-h{font-size:32px;font-weight:600}
.section-p{left:110px;width:980px;text-align:center;font-size:16px;line-height:29px;color:#444}
.card{position:absolute;top:2452px;width:336px;height:363px;background:var(--white);padding:22px 22px}
.card h3{font-family:"Exo 2",sans-serif;font-weight:600;font-size:23px;color:var(--ink);margin:20px 0 14px}
.card p{font-size:16px;line-height:29px;text-align:justify;color:#444}

/* steps */
.steps-band{left:0;top:3285px;width:1200px;height:627px;background:linear-gradient(135deg,var(--green),var(--green-dark))}
.step-num{position:absolute;top:3241px;width:108px;height:108px;border-radius:50%;background:var(--white);font-family:"Exo 2",sans-serif;font-weight:700;font-size:50px;color:var(--ink);display:flex;align-items:center;justify-content:center}
.step-title{position:absolute;top:3384px;width:340px;text-align:center;font-weight:700;font-size:24px;color:var(--white)}
.step-img{position:absolute;top:3454px;width:322px;height:165px;background:linear-gradient(160deg,#5a5a5a,#c9c9c9 60%,#7a7a7a)}
.step-text{position:absolute;top:3643px;width:340px;text-align:center;color:var(--white);font-size:16px;line-height:29px}

/* badges */
.badge{position:absolute;top:4021px;width:156px;height:156px;border-radius:50%}

/* contact */
.contact{left:0;top:4293px;width:1200px;height:646px;background:linear-gradient(135deg,#1d1d1d,#141414 50%,#1f1f1f)}
.ct{position:absolute;color:var(--white)}
.ct-btn{position:absolute;border:1.5px solid #bbb;color:var(--white);font-size:16px;display:flex;align-items:center;justify-content:center}
.map{left:635px;top:4733px;width:333px;height:118px;border:1.5px dashed #aaa;border-radius:14px;background:linear-gradient(135deg,#3a3f44,#5b6166);display:flex;align-items:center;justify-content:center;color:var(--white);font-size:19px;text-decoration:underline}

/* footer */
.footer{left:0;top:4939px;width:1200px;height:375px;background:var(--footer)}
.f-h{position:absolute;top:5002px;color:var(--white);font-family:"Exo 2",sans-serif;font-weight:700;font-size:17px}
.f-list{position:absolute;top:5034px;color:#ddd;font-size:14.5px;line-height:29px;list-style:none}
.f-list li{display:flex;gap:10px;align-items:flex-start}
.social{position:absolute;top:5094px;width:22px;height:22px;border-radius:50%;background:#2d6fd6}
.chat-bot{left:1056px;top:4882px;width:76px;height:48px;border-radius:24px;background:#e9eef8}
.chat-tip{left:976px;top:4922px;width:164px;height:44px;border:1px solid #555;border-radius:6px;background:#1b1b1b;color:#ccc;font-size:12.5px;display:flex;align-items:center;justify-content:center}
</style>
</head>
<body>

<!-- hero -->
<section class="abs hero" role="img" aria-label="Photo of three lawyers in an office holding coffee cups"></section>
<div class="abs brand"><div class="mark"></div>KELLBROOK<br>LAWYERS</div>
<nav class="abs nav"><span>What should i do now?</span><span>About</span><span>Lawyers</span><span>Practice Areas</span><span>Cases</span><span>Contact</span></nav>
<div class="abs nav-phone"><svg width="16" height="16" viewBox="0 0 24 24"><path fill="#fff" d="M6.6 10.8a15 15 0 0 0 6.6 6.6l2.2-2.2c.3-.3.7-.4 1-.2 1.1.4 2.3.6 3.6.6.6 0 1 .4 1 1V20c0 .6-.4 1-1 1A17 17 0 0 1 3 4c0-.6.4-1 1-1h3.5c.6 0 1 .4 1 1 0 1.3.2 2.5.6 3.6.1.3 0 .7-.2 1z"/></svg>(+1) 555 010 0199</div>
<h1 class="abs centered head hero-title">Welcome To<br>Kellbrook Lawyers</h1>
<div class="hero-btn" style="left:403px;width:188px"><svg width="22" height="18" viewBox="0 0 22 18"><rect x="1" y="1" width="20" height="13" rx="2" fill="none" stroke="#fff" stroke-width="1.6"/><path d="M5 14v3l4-3" fill="none" stroke="#fff" stroke-width="1.6"/></svg>MESSAGE US</div>
<div class="hero-btn" style="left:607px;width:188px"><svg width="18" height="18" viewBox="0 0 24 24"><path fill="none" stroke="#fff" stroke-width="1.8" d="M6.6 10.8a15 15 0 0 0 6.6 6.6l2.2-2.2c.3-.3.7-.4 1-.2 1.1.4 2.3.6 3.6.6.6 0 1 .4 1 1V20c0 .6-.4 1-1 1A17 17 0 0 1 3 4c0-.6.4-1 1-1h3.5c.6 0 1 .4 1 1 0 1.3.2 2.5.6 3.6.1.3 0 .7-.2 1z"/></svg>CALL US NOW</div>
<div class="abs centered hero-cta">Click Video To Learn More</div>
<div class="abs video-main" role="img" aria-label="Video still of the legal team standing with arms crossed">
  <div class="play" style="left:341px;top:160px;width:60px;height:60px"><svg width="22" height="24" viewBox="0 0 22 24"><path d="M3 2l17 10L3 22z" fill="#111"/></svg></div>
</div>

<!-- welcome -->
<h2 class="abs centered head welcome-h">Welcome to Kellbrook Lawyers</h2>
<p class="abs welcome-sub">Lorem ipsum dolor sit amet, consectetur adipiscing elit, sed do eiusmod tempor incididunt ut labore et dolore magna aliqua.</p>
<p class="abs col" style="left:112px">Lorem ipsum dolor sit amet, consectetur adipiscing elit, sed do eiusmod tempor incididunt ut labore et dolore magna aliqua. Quis ipsum suspendisse ultrices gravida. Risus commodo viverra maecenas accumsan lacus vel facilisis. Lorem ipsum dolor sit amet, consectetur adipiscing elit, sed do eiusmod tempor incididunt ut labore et dolore magna aliqua. Quis ipsum suspendisse ultrices gravida.</p>
<p class="abs col" style="left:615px">Lorem ipsum dolor sit amet, consectetur adipiscing elit, sed do eiusmod tempor incididunt ut labore et dolore magna aliqua. Quis ipsum suspendisse ultrices gravida. Risus commodo viverra maecenas accumsan lacus vel facilisis. Lorem ipsum dolor sit amet, consectetur adipiscing elit, sed do eiusmod tempor incididunt ut labore et dolore magna aliqua. Quis ipsum suspendisse ultrices gravida.</p>

<!-- reviews -->
<section class="abs reviews">
  <div class="arrow-c" style="left:48px;top:117px"><svg width="10" height="12"><path d="M8 1L2 6l6 5" fill="none" stroke="#111" stroke-width="1.6"/></svg></div>
  <div class="arrow-c" style="left:1121px;top:117px"><svg width="10" height="12"><path d="M2 1l6 5-6 5" fill="none" stroke="#111" stroke-width="1.6"/></svg></div>
  <div class="abs head" style="left:113px;top:92px;font-size:22px;font-weight:600">Excellence</div>
  <div class="abs" style="left:113px;top:122px;color:var(--star);font-size:24px;letter-spacing:2px">★★★★★</div>
  <div class="review" style="left:297px"><div style="color:var(--star);letter-spacing:2px">★★★★★</div><div class="name">Sam Carter</div>Lorem ipsum dolor sit amet, consectetur adipiscing elit, sed do eiusmod tempor incididunt.</div>
  <div class="review" style="left:572px"><div style="color:var(--star);letter-spacing:2px">★★★★★</div><div class="name">Sam Carter</div>Lorem ipsum dolor sit amet, consectetur adipiscing elit, sed do eiusmod tempor incididunt.</div>
  <div class="review" style="left:847px"><div style="color:var(--star);letter-spacing:2px">★★★★★</div><div class="name">Sam Carter</div>Lorem ipsum dolor sit amet, consectetur adipiscing elit, sed do eiusmod tempor incididunt.</div>
</section>

<!-- stats -->
<div class="stat" style="left:61px;top:2018px">OVER<div class="num">8400</div>COURTROOM HOURS</div>
<div class="stat" style="left:443px;top:2018px">MORE THAN<div class="num">1000</div>CLIENTS HELPED</div>
<div class="stat" style="left:832px;top:2002px">WE HAVE<div class="num">50+</div>YEARS OF CRIMINAL<br>DEFENCE EXPERIENCE</div>

<!-- practice -->
<section class="abs practice"></section>
<h2 class="abs centered head section-h" style="top:2288px">Practice Areas</h2>
<p class="abs section-p" style="top:2351px">Lorem ipsum dolor sit amet, consectetur adipiscing elit, sed do eiusmod tempor incididunt ut labore et dolore magna aliqua. Quis ipsum suspendisse ultrices gravida. Risus commodo viverra maecenas accumsan lacus vel facilisis.</p>

<div class="card" style="left:74px">
  <svg width="40" height="40" viewBox="0 0 40 40"><circle cx="14" cy="14" r="9" fill="none" stroke="#111" stroke-width="2"/><circle cx="24" cy="20" r="7" fill="none" stroke="#111" stroke-width="2"/><path d="M16 28l-6 8" stroke="#111" stroke-width="2"/></svg>
  <h3>Criminal Law</h3>
  <p>Lorem ipsum dolor sit amet, consectetur adipiscing elit, sed do eiusmod tempor incididunt ut labore et dolore magna aliqua. Quis ipsum suspendisse ultrices gravida.</p>
</div>
<div class="card" style="left:431px">
  <svg width="40" height="40" viewBox="0 0 40 40"><circle cx="12" cy="8" r="4" fill="none" stroke="#111" stroke-width="2"/><circle cx="28" cy="8" r="4" fill="none" stroke="#111" stroke-width="2"/><path d="M4 36V20a8 8 0 0 1 16 0v16M20 36V20a8 8 0 0 1 16 0v16" fill="none" stroke="#111" stroke-width="2"/></svg>
  <h3>Family Law</h3>
  <p>Lorem ipsum dolor sit amet, consectetur adipiscing elit, sed do eiusmod tempor incididunt ut labore et dolore magna aliqua. Quis ipsum suspendisse ultrices gravida.</p>
</div>
<div class="card" style="left:786px">
  <svg width="40" height="40" viewBox="0 0 40 40"><path d="M4 18L20 4l16 14v18H4z" fill="none" stroke="#111" stroke-width="2"/><rect x="14" y="20" width="12" height="16" fill="none" stroke="#111" stroke-width="2"/></svg>
  <h3>Civil Litigation</h3>
  <p>Lorem ipsum dolor sit amet, consectetur adipiscing elit, sed do eiusmod tempor incididunt ut labore et dolore magna aliqua. Quis ipsum suspendisse ultrices gravida.</p>
</div>
<div class="btn-outline" style="left:151px;top:2750px;width:170px;height:42px">Learn More <svg width="18" height="12"><path d="M0 6h16M11 1l5 5-5 5" fill="none" stroke="#111" stroke-width="1.6"/></svg></div>
<div class="btn-outline" style="left:508px;top:2750px;width:170px;height:42px">Learn More <svg width="18" height="12"><path d="M0 6h16M11 1l5 5-5 5" fill="none" stroke="#111" stroke-width="1.6"/></svg></div>
<div class="btn-outline" style="left:863px;top:2750px;width:170px;height:42px">Learn More <svg width="18" height="12"><path d="M0 6h16M11 1l5 5-5 5" fill="none" stroke="#111" stroke-width="1.6"/></svg></div>
<div class="btn-outline" style="left:532px;top:2856px;width:136px;height:40px">View More</div>

<!-- steps -->
<h2 class="abs centered head section-h" style="top:3038px">Steps When Facing A Criminal Charge</h2>
<p class="abs section-p" style="top:3100px">Lorem ipsum dolor sit amet, consectetur adipiscing elit, sed do eiusmod tempor incididunt ut labore et dolore magna aliqua. Quis ipsum suspendisse ultrices gravida. Risus commodo viverra maecenas accumsan lacus vel facilisis.</p>
<section class="abs steps-band"></section>
<div class="step-num" style="left:194px">1</div>
<div class="step-num" style="left:546px">2</div>
<div class="step-num" style="left:897px">3</div>
<div class="step-title" style="left:78px">Analysis &amp; Strategize</div>
<div class="step-title" style="left:430px">Negotiation</div>
<div class="step-title" style="left:781px">Advocacy At Trial</div>
<div class="step-img" style="left:87px" role="img" aria-label="Video still of a lawyer reviewing documents with a client"><div class="play" style="left:143px;top:64px;width:36px;height:36px"><svg width="12" height="14" viewBox="0 0 22 24"><path d="M3 2l17 10L3 22z" fill="#111"/></svg></div></div>
<div class="step-img" style="left:437px" role="img" aria-label="Video still of a negotiation meeting at a desk"><div class="play" style="left:143px;top:64px;width:36px;height:36px"><svg width="12" height="14" viewBox="0 0 22 24"><path d="M3 2l17 10L3 22z" fill="#111"/></svg></div></div>
<div class="step-img" style="left:790px" role="img" aria-label="Video still of a lawyer speaking with a client"><div class="play" style="left:143px;top:64px;width:36px;height:36px"><svg width="12" height="14" viewBox="0 0 22 24"><path d="M3 2l17 10L3 22z" fill="#111"/></svg></div></div>
<p class="step-text" style="left:78px">Lorem ipsum dolor sit amet, consectetur adipiscing elit, sed do eiusmod tempor incididunt ut labore et dolore magna aliqua.</p>
<p class="step-text" style="left:430px">Lorem ipsum dolor sit amet, consectetur adipiscing elit, sed do eiusmod tempor incididunt ut labore et dolore magna aliqua.</p>
<p class="step-text" style="left:781px">Lorem ipsum dolor sit amet, consectetur adipiscing elit, sed do eiusmod tempor incididunt ut labore et dolore magna aliqua.</p>
<div class="btn-outline" style="left:428px;top:3820px;width:160px;height:42px;border-color:#fff">See Next Steps</div>
<div class="btn-outline" style="left:624px;top:3820px;width:160px;height:42px;border-color:#fff;background:transparent;color:#fff">Contact Us</div>

<!-- certifications -->
<div class="badge" style="left:136px;background:#1f8a3a"></div>
<div class="badge" style="left:330px;background:#1f8a80"></div>
<div class="badge" style="left:522px;background:#2a7d6e"></div>
<div class="badge" style="left:714px;background:#c23a2e"></div>
<div class="badge" style="left:908px;background:#e2821c"></div>

<!-- contact -->
<section class="abs contact"></section>
<div class="ct head" style="left:111px;top:4393px;font-size:30px;font-weight:600;color:#fff;letter-spacing:1px">MARTIN J.ELLERY</div>
<div class="ct head" style="left:111px;top:4437px;font-size:22px;font-weight:600;color:#fff">Principal Lawyer</div>
<div class="ct head" style="left:111px;top:4491px;font-size:22px;font-weight:600;color:#fff">Call 24/7 For A Free Consultation</div>
<div class="ct head" style="left:111px;top:4522px;font-size:44px;font-weight:700;color:#fff;letter-spacing:2px">1300 555 019</div>
<div class="ct-btn" style="left:111px;top:4598px;width:246px;height:44px">Book A Scheduled Meeting</div>
<div class="ct head" style="left:633px;top:4385px;font-size:22px;font-weight:600;color:#fff">Enquire With Us</div>
<div class="ct-btn" style="left:635px;top:4436px;width:354px;height:50px;justify-content:flex-start;padding-left:26px;font-size:15px">Email</div>
<div class="ct-btn" style="left:635px;top:4508px;width:162px;height:42px">Contact Us</div>
<div class="abs" style="left:111px;top:4715px;width:1010px;height:1px;background:#444"></div>
<div class="ct head" style="left:113px;top:4732px;font-size:22px;font-weight:600;color:#fff">Our Business Location</div>
<div class="ct" style="left:113px;top:4777px;width:400px;font-size:15px;line-height:28px">Suite 12, Ground Floor, 88 Harbour Lane, Melbourne VIC 3000.</div>
<div class="abs map" role="img" aria-label="Map showing the office location">Click To See Map</div>

<!-- footer -->
<section class="abs footer"></section>
<div class="abs" style="left:111px;top:5000px;width:130px;text-align:center;color:#fff;font-weight:700;font-size:18px;line-height:1.1;letter-spacing:1px"><div style="width:36px;height:36px;border-radius:50%;border:2px solid #fff;margin:0 auto 8px"></div>KELLBROOK<br>LAWYERS</div>
<div class="social" style="left:126px;background:#555"></div>
<div class="social" style="left:160px"></div>
<div class="social" style="left:194px"></div>
<div class="f-h" style="left:293px">Practice Areas</div>
<ul class="f-list" style="left:293px"><li>Criminal Law</li><li>Family Law</li><li>Civil Litigation</li><li>Wills &amp; Probate</li><li>BRUNE Claims</li></ul>
<div class="f-h" style="left:514px">Quick Links</div>
<ul class="f-list" style="left:514px"><li>What should i do now?</li><li>About</li><li>Lawyers</li><li>Practice Areas</li><li>Cases</li><li>Contact</li></ul>
<div class="f-h" style="left:746px">Contact</div>
<ul class="f-list" style="left:746px;width:360px">
  <li><span style="color:#fff">☎</span>0400 555 118</li>
  <li><span style="color:#fff">✉</span>mellery@kellbrooklawyers.com.au</li>
  <li><span style="color:#fff">●</span>kellbrooklawyers.com.au</li>
  <li><span style="color:#fff">⚲</span><span>Suite 12, Ground Floor, 88 Harbour Lane,<br>Melbourne VIC 3000. <span style="color:var(--green);text-decoration:underline">Click To See Map</span></span></li>
  <li><span style="color:#fff">▣</span>ABN: 12 345 678 901</li>
</ul>
<div class="abs" style="left:0;top:5262px;width:1200px;height:1px;background:#333"></div>
<div class="abs centered" style="top:5278px;color:#ddd;font-size:15px">© Copyrights 2023 Kellbrook Lawyers | All Rights Reserved</div>

<!-- chat -->
<div class="abs chat-bot" role="img" aria-label="Chat assistant icon"></div>
<div class="abs chat-tip">Hey There! Talk To Us!</div>

</body>
</html>
```